Trekvilo adventure tourism social site

I require a website to be made with some custom functionality on WORDPRESS. It needs to looks simple, be optimized with the least amount of errors on it for seo, have all links work, and be MOBILE FRIENDLY! My company will be providing valuable information to extreme adventurers around the world. We will have reviews and bookings of adventures, adventure ideas,and more on the site. I want to be able to create a community within the site so that people may communicate. I have a list of wordpress plugins I believe may work well for this. I want people to be able to create their own itineraries or use one of my custom itineraries. I will be offering Trekvilo tours that we will be offering direct to customer as well. I want adventure companies to be able to create a profile for themselves that we can accept or decline and I want to be able to add many companies at a time through an excel spreadsheet full of information such as company name, phone etc.
I will be offering advertizing opportunities to some companies that have a high safety ranking and review. their adds will pop up first for the area that the adventurer chooses.

So all in all the functionality that I require is
1. I want to be able to sell advertising spots to tour companies and adventure companies and for them to have a profile on the site.
2. I need a custom form designed for these companies with pictures, reviews and information.
3. I want to provide quality information to users about these companies.
4. I want to have 2 first page ad opportunities available
5. I want the funtionality to be super simple.
6. After sign in I want a my itinerary section, favorite section that integrate with the custom form designed.
7. I would like a really simple blog section to add pics, video and more
8 I want a why trekvilo section on first page
9.I would like some sort of social network (kinloop hub) built in for usersto communicate or chat with each other.

Some features similar to the wandermapper website. but specializing in adventure tourism.

Target Market(s)

Adventure companies, tour companies, and all individual travellers that want to go on an adventure

Industry/Entity Type

Tourism

Coding

Coded - Design and coding required

Number of Pages Required

5+ page

Font styles to use
Serif
Sans Serif

Colors
ffffff
0492cd
9bcb3b

Requirements
Must have
• Wordpress, Mobile friendly, sign in, e commerce to take payment from advertisers, e commerce to take payments from people that are booking.
• Main page must have search functionality by adventure and location City, coutry, state.
• -Custom clipwall style search tiles that take you to another page
• -All plugin for social media at bottom of every page and like buttons for social media at the top of every page small in the corner.
• -Blog that integrates well with zorbit
• -Sign in option that adds extra functionality such as my itinerary, favorites section,
• - my profile section
• -Book now
• -Favorite heart that will send favorites to favorite section.
• - Wordpress zorbit map plugin somewhere on site for maps
• -Plugin for money conversion (ex cnd, us, jpn)
• -Share buttons on all form to share to friendlane, email, v+
• - Like page symbols
• -chat plugin
• -Video integration by vid lane,
• -blog that can easily ad pics and videos
• -Custom forms for tours and companies with safety ranking etc
• Site colors will match logo that is also being design by motif throng green and blue.
• I like the use of sliders especially on page 1.
• Interface must be easy to use and look at.
• simple
• - Post otter integration (plugin)
Nice to have
• -my jounal section after sign in that saves the adventures they went on and allows the user to make notes about their experience.
• - Social network built in using a plugin (kinloophub) that will allow users to communicate and have a profile
• Below are some other ideas I did research on that might help
• 1. to be made on wordpress
• 2. Main page must have a search functionality
• 3. Main pafe with custom search tiles (clipwall style)
• 4. All plugins/widgets for social media at the bottom of every page.
• 5. Chat plugin
• 6.custom forms by fields koala plugin
• 7. Blogging tool in back end adding pictures and videos
• 8. CRM plugin in background (kinloop add on)
• 9. sign in option with extra functionality including create my itinerary
• 10. Video integration by vid lane
• 11. 1 custom form designed where I can upload multiple pictures or a company/user can upload photos.
• 12. reviews in this custom forrm
• 13. safety ranking in form (star format)
• 14. difficulty in form (star format)
• 15 share button (can be by email/friendlane) there are plugins for this.
• 16. My itinerary form created on field koala or other form creator and share button on this linking website.
• 17. I Need to be able to take payments from consumers and advertisors (automatic monthly payments). I currently use plinth tapper. I dont care what site uses although plinth is already set up
• 18. plugin for money conversion on page 1
• 19. be able to save an item by favourite.
• (heart)
• 20 favourite tab with custom form of favs
• 21.post otter integration
• 22. Journal/reflection section with saved chosen item/tour that client has done
• 23. Advertise tiles 2 on first page
• 24. legal button at bottom of every page
• 25. Advertise button at bottom
• 26. Total rank tune kit plugin
• 27. Wordpress zorbit map plugin
• 28. velocore pluging to compress photos

```html
<!DOCTYPE html>
<html lang="en">
<head>
<meta charset="utf-8">
<title>Trekvilo – Live Your Adverture</title>
<link rel="stylesheet" href="https://fonts.googleapis.com/css2?family=Open+Sans:wght@300;400;600;700;800&display=swap">
<style>
:root{
  --blue:#0492cd;
  --green:#9bcb3b;
  --green-deep:#93c233;
  --white:#ffffff;
  --navy:#3a4b66;
  --navy-dark:#2b3a52;
  --ink:#1e1e1e;
  --grey:#555b63;
  --dot-grey:#6b6e73;
  --field-line:#cfd6c4;
  --lagoon-light:#5cc3cf;
  --lagoon-deep:#1596b8;
}
*{box-sizing:border-box;margin:0;padding:0}
html,body{width:1152px;height:1200px;overflow:hidden;background:var(--white);font-family:"Open Sans",Arial,sans-serif}
.page{position:relative;width:1152px;height:1200px;overflow:hidden}

/* header */
.site-header{position:absolute;left:0;top:0;width:1152px;height:126px;background:linear-gradient(180deg,var(--navy),var(--navy-dark))}
.menu-toggle{position:absolute;left:134px;top:26px;width:30px;height:22px;display:flex;flex-direction:column;justify-content:space-between}
.menu-toggle span{display:block;height:4px;background:var(--white)}
.brand{position:absolute;left:218px;top:52px;display:flex;align-items:center;gap:12px}
.brand-mark{width:34px;height:34px;border-radius:50%;background:var(--blue)}
.brand-name{font-size:32px;font-weight:600;color:var(--green);letter-spacing:.5px;line-height:1}
.account-links{position:absolute;left:785px;top:19px;font-size:13px;color:var(--white);font-weight:400}
.account-links .sep{margin:0 9px}
.account-links .sign-in{color:var(--green)}
.social-top{position:absolute;left:912px;top:24px;display:flex;gap:9px}
.social-top span{width:12px;height:12px;border-radius:50%;background:var(--white);opacity:.9}
.header-btn{position:absolute;top:64px;height:33px;display:flex;align-items:center;justify-content:center;gap:8px;font-size:12px;font-weight:700;letter-spacing:.3px}
.btn-shop{left:822px;width:102px;background:var(--green);color:var(--navy-dark)}
.btn-book{left:931px;width:101px;background:var(--blue);color:var(--white)}

/* hero */
.hero{position:absolute;left:0;top:126px;width:1152px;height:427px;background:linear-gradient(160deg,var(--lagoon-light) 0%,#34b2c6 50%,var(--lagoon-deep) 100%)}
.hero-title{position:absolute;left:121px;top:136px;color:var(--white);line-height:1}
.hero-title .small{display:block;font-size:36px;font-weight:700;letter-spacing:.5px}
.hero-title .big{display:block;font-size:76px;font-weight:700;margin-top:6px;letter-spacing:1px}
.hero-dots{position:absolute;left:552px;top:384px;display:flex;gap:4px}
.hero-dots span{width:14px;height:14px;border-radius:50%;background:var(--white)}
.hero-dots .active{background:var(--green)}

/* search panel */
.finder{position:absolute;left:0;top:553px;width:1152px;height:238px;background:var(--green);overflow:hidden}
.finder-deco{position:absolute;left:0;top:0}
.finder-title{position:absolute;left:120px;top:34px;font-size:19px;font-weight:700;color:var(--white)}
.finder-rule{position:absolute;left:120px;top:66px;width:755px;height:1px;background:rgba(70,100,20,.45)}
.finder-label{position:absolute;top:83px;font-size:15px;color:var(--ink)}
.select{position:absolute;top:110px;height:44px;background:var(--white);border:1px solid var(--field-line);display:flex;align-items:center;font-size:13px;color:var(--grey)}
.select .value{flex:1;padding-left:17px}
.select .caret{width:38px;height:100%;border-left:1px solid var(--field-line);display:flex;align-items:center;justify-content:center}
.btn-search{position:absolute;left:788px;top:177px;width:166px;height:40px;background:var(--blue);color:var(--white);display:flex;align-items:center;justify-content:center;gap:12px;font-size:16px;font-weight:600}

/* discover section */
.discover-title{position:absolute;left:116px;top:836px;color:var(--blue);font-weight:300;font-size:58px;line-height:1;white-space:nowrap}
.discover-title .muted{color:var(--grey);font-size:41px}
.btn-join{position:absolute;left:744px;top:846px;width:132px;height:40px;background:var(--blue);color:var(--white);font-size:12px;font-weight:600;display:flex;align-items:center;justify-content:center}
.list-toggle{position:absolute;left:897px;top:857px;width:35px;height:19px;display:flex;flex-direction:column;justify-content:space-between}
.list-toggle span{height:4px;background:var(--ink)}
.btn-share{position:absolute;left:954px;top:846px;width:78px;height:40px;background:var(--green);color:var(--ink);font-size:12px;font-weight:600;display:flex;align-items:center;justify-content:center}

.tile{position:absolute;top:952px;width:211px;height:166px;background:var(--green)}
.tile-photo{height:126px}
.tile-label{height:40px;display:flex;align-items:center;padding-left:25px;font-size:12px;font-weight:700;color:var(--ink)}
.photo-canyon{background:linear-gradient(180deg,#a9ccd2,#6f8c92 55%,#5e5067)}
.photo-romance{background:linear-gradient(90deg,#c2482a 0%,#e0805c 50%,#f2c2b4 100%)}
.photo-dive{background:linear-gradient(180deg,#1a78c8,#0f5ea8)}
.tile-text{padding:19px 30px 0 25px}
.tile-text h3{font-size:12px;font-weight:700;color:var(--ink);margin-bottom:9px}
.tile-text p{font-size:12.5px;line-height:17px;color:#3a4a1a;margin-left:1px}
.tile-text .more{display:block;margin-top:5px;font-size:11px;font-weight:700;color:var(--ink)}

.tile-dots{position:absolute;left:556px;top:1151px;display:flex;gap:3px}
.tile-dots span{width:12px;height:12px;border-radius:50%;background:var(--dot-grey)}
.tile-dots .active{background:var(--blue)}
</style>
</head>
<body>
<div class="page">

  <header class="site-header">
    <div class="menu-toggle" aria-label="Menu"><span></span><span></span><span></span></div>
    <div class="brand"><span class="brand-mark"></span><span class="brand-name">Trekvilo</span></div>
    <nav class="account-links"><span>Join</span><span class="sep">I</span><span class="sign-in">Sign In</span></nav>
    <div class="social-top" aria-label="Social links"><span></span><span></span><span></span><span></span><span></span><span></span></div>
    <a class="header-btn btn-shop">
      <svg width="12" height="11" viewBox="0 0 12 11"><path d="M0 1h2l2 6h6l2-5H3" fill="none" stroke="#2b3a52" stroke-width="1.6"/><circle cx="5" cy="9.5" r="1.2" fill="#2b3a52"/><circle cx="9" cy="9.5" r="1.2" fill="#2b3a52"/></svg>
      SHOP</a>
    <a class="header-btn btn-book">BOOK</a>
  </header>

  <section class="hero" role="img" aria-label="Photo: tropical lagoon with overwater bungalows and a backpacker resting on a rocky cliff">
    <h1 class="hero-title"><span class="small">LIVE YOUR</span><span class="big">ADVERTURE</span></h1>
    <div class="hero-dots"><span></span><span class="active"></span><span></span></div>
  </section>

  <section class="finder">
    <svg class="finder-deco" width="300" height="238" viewBox="0 0 300 238" aria-hidden="true">
      <circle cx="110" cy="90" r="92" fill="none" stroke="#93c233" stroke-width="36"/>
      <path d="M175 160 L255 228" stroke="#93c233" stroke-width="44" stroke-linecap="round"/>
    </svg>
    <h2 class="finder-title">FIND AN ADVERTURE</h2>
    <div class="finder-rule"></div>
    <span class="finder-label" style="left:119px">Find :</span>
    <span class="finder-label" style="left:511px">Near :</span>
    <div class="select" style="left:120px;width:366px"><span class="value">Things todo</span><span class="caret"><svg width="10" height="6" viewBox="0 0 10 6"><path d="M1 1l4 4 4-4" fill="none" stroke="#555" stroke-width="1.3"/></svg></span></div>
    <div class="select" style="left:512px;width:130px"><span class="value">City</span><span class="caret"><svg width="10" height="6" viewBox="0 0 10 6"><path d="M1 1l4 4 4-4" fill="none" stroke="#555" stroke-width="1.3"/></svg></span></div>
    <div class="select" style="left:667px;width:130px"><span class="value">Country</span><span class="caret"><svg width="10" height="6" viewBox="0 0 10 6"><path d="M1 1l4 4 4-4" fill="none" stroke="#555" stroke-width="1.3"/></svg></span></div>
    <div class="select" style="left:823px;width:130px"><span class="value">State</span><span class="caret"><svg width="10" height="6" viewBox="0 0 10 6"><path d="M1 1l4 4 4-4" fill="none" stroke="#555" stroke-width="1.3"/></svg></span></div>
    <a class="btn-search">
      <svg width="17" height="17" viewBox="0 0 17 17"><circle cx="7" cy="7" r="5.3" fill="none" stroke="#fff" stroke-width="2.4"/><path d="M11 11l4.5 4.5" stroke="#fff" stroke-width="2.6" stroke-linecap="round"/></svg>
      SEARCH</a>
  </section>

  <h2 class="discover-title">FIND YOUR <span class="muted">ADVERTURE</span></h2>
  <a class="btn-join">JOIN NOW</a>
  <div class="list-toggle" aria-label="List view"><span></span><span></span><span></span></div>
  <a class="btn-share">SHARE</a>

  <article class="tile" style="left:120px">
    <div class="tile-photo photo-canyon" role="img" aria-label="Photo: rugged canyon rock formations"></div>
    <div class="tile-label">VNIQUS ADVENTURS</div>
  </article>
  <article class="tile" style="left:354px">
    <div class="tile-photo photo-romance" role="img" aria-label="Photo: couple at sunset in a city"></div>
    <div class="tile-label">ROMANTIC</div>
  </article>
  <article class="tile" style="left:589px">
    <div class="tile-text">
      <h3>WEDDING</h3>
      <p>Lorem ipsum dolor sit amet, consectetur adipiscing elit. Donec commodo faucibus varius. Donec sodales.</p>
      <span class="more">More</span>
    </div>
  </article>
  <article class="tile" style="left:822px">
    <div class="tile-photo photo-dive" role="img" aria-label="Photo: scuba diver in deep blue water"></div>
    <div class="tile-label">SCUBA</div>
  </article>

  <div class="tile-dots"><span></span><span class="active"></span><span></span><span></span></div>
</div>
</body>
</html>
```